Package Card - Horse Products

I require a card design for the top of a package (see photo). This product is a number holder that gets pinned on to a horse bridle or saddle blanket for competitions. It is a high quality, genuine leather, and premium product.Card is 15cm across and 6cm high. Requirements:Must have - Logo, -"Equestrian Number Holder"- Place on back for barcodeAnything else is up to you! Suggestions and ideas welcome. Card back colour can be any colour.My outcome is for it to look like a premium product

Target Market(s)

High end equestrian competitors

Colors
fbf289

Requirements
Must have
• Logo
• "Equestrian Number Holder"
• "Genuine Leather"
• Room on the back for a barcode sticker
Nice to have
• Should look up market and elegant

```html
<!DOCTYPE html>
<html lang="en">
<head>
<meta charset="utf-8">
<title>Tidewater Equestrian – Number Holder Header Card</title>
<link href="https://fonts.googleapis.com/css2?family=PT+Sans+Narrow:wght@400;700&display=swap" rel="stylesheet">
<style>
  :root {
    --backdrop: #e9e9ec;
    --card-black: #050505;
    --gold: #e0ac45;
    --gold-band: #f2bb55;
    --gold-deep: #b9862c;
    --ink: #121212;
    --white: #f4f4f4;
  }
  * { margin: 0; padding: 0; box-sizing: border-box; }
  html, body {
    width: 1200px;
    height: 770px;
    overflow: hidden;
    background: var(--backdrop);
    font-family: "PT Sans Narrow", "Arial Narrow", sans-serif;
  }
  .header-card {
    position: absolute;
    left: 50px;
    top: 165px;
    width: 1100px;
    height: 440px;
    background: var(--card-black);
    overflow: hidden;
  }
  .dot-field {
    position: absolute;
    right: 0;
    top: 0;
    width: 480px;
    height: 340px;
    background: radial-gradient(ellipse at 100% 0%, var(--gold) 0%, rgba(224,172,69,0.55) 30%, rgba(185,134,44,0.18) 60%, rgba(5,5,5,0) 80%);
  }
  .hang-hole {
    position: absolute;
    left: 526px;
    top: 52px;
    width: 30px;
    height: 30px;
    border-radius: 50%;
    background: var(--backdrop);
  }
  .brand-name {
    position: absolute;
    left: 0;
    width: 1100px;
    top: 150px;
    text-align: center;
    color: var(--gold);
    font-weight: 400;
    font-size: 50px;
    letter-spacing: 3px;
    text-transform: uppercase;
  }
  .product-band {
    position: absolute;
    left: 198px;
    top: 268px;
    width: 682px;
    height: 86px;
    background: var(--gold-band);
    display: flex;
    align-items: center;
    justify-content: center;
  }
  .product-name {
    color: var(--ink);
    font-weight: 700;
    font-size: 50px;
    letter-spacing: 0.3px;
  }
  .material-note {
    position: absolute;
    left: 0;
    width: 1100px;
    top: 378px;
    text-align: center;
    color: var(--white);
    font-weight: 400;
    font-size: 26px;
  }
</style>
</head>
<body>
  <main class="header-card">
    <div class="dot-field" role="img" aria-label="Gold halftone dot pattern fading from the top right corner"></div>
    <div class="hang-hole"></div>
    <div class="brand-name">Tidewater Equestrian</div>
    <div class="product-band"><h1 class="product-name">Equestrian Number Holder</h1></div>
    <p class="material-note">Genuine Leather</p>
  </main>
</body>
</html>
```